Conceptual Model Diagram for Replacing Medication with Behavior to Support Weight Loss Maintenance

Design a figure of a conceptual model that needs to be inserted into a word document for a PSF grant. This conceptual model illustrates how behavioral strategies can replace the regulatory functions lost after AOM discontinuation. The intervention targets three core vulnerabilities—appetite resurgence, metabolic inflexibility, and suboptimal mindstate—through the domains of Food, Physical Activity, and Mind. Sustained weight loss maintenance occurs at the intersection of these domains. The intervention is delivered within a design framework that makes behaviors easier to perform, aligns them with identity, and reinforces them through virtual support and community, ensuring real-world feasibility and long-term adherence.
Target Market(s)
PSF reviewers
Industry/Entity Type
academic
Other font styles liked:
- arial
Requirements
Must have
- see my attached description

```html
<!DOCTYPE html>
<html lang="en">
<head>
<meta charset="utf-8">
<title>Conceptual Model: Replacing Medication with Behavior for Weight Loss Maintenance</title>
<link rel="stylesheet" href="https://fonts.googleapis.com/css2?family=Barlow+Semi+Condensed:wght@600&family=Poppins:wght@300;700&display=swap">
<style>
  :root {
    --bg: #ffffff;
    --ink: #3c3c3c;
    --label: #474747;
    --dash: #4d4d4d;
    --band: #f1f1f1;
    --domain: #8a8c92;
  }
  html, body {
    margin: 0;
    padding: 0;
    width: 1200px;
    height: 1200px;
    overflow: hidden;
    background: var(--bg);
  }
  .model {
    display: block;
    width: 1200px;
    height: 1200px;
  }
  .ring-dashed {
    fill: none;
    stroke: var(--dash);
    stroke-width: 1;
    stroke-dasharray: 7 5;
  }
  .ring-band {
    fill: none;
    stroke: var(--band);
    stroke-width: 40;
  }
  .domain {
    fill: var(--domain);
    fill-opacity: 0.2;
  }
  .ring-text {
    font-family: "Poppins", Arial, sans-serif;
    font-weight: 300;
    font-size: 18px;
    fill: var(--ink);
  }
  .ring-text .sep { font-weight: 700; }
  .domain-label {
    font-family: "Barlow Semi Condensed", Arial, sans-serif;
    font-weight: 600;
    font-size: 17px;
    fill: var(--label);
    text-anchor: middle;
  }
  .outcome-label {
    font-family: "Barlow Semi Condensed", Arial, sans-serif;
    font-weight: 600;
    font-size: 13.5px;
    fill: var(--label);
    text-anchor: middle;
  }
  .vulnerability {
    font-family: "Barlow Semi Condensed", Arial, sans-serif;
    font-weight: 600;
    font-size: 11.5px;
    fill: var(--label);
    text-anchor: middle;
  }
  .pointer {
    stroke: var(--label);
    stroke-width: 1;
    fill: none;
    marker-end: url(#arrowhead);
  }
</style>
</head>
<body>
<svg class="model" viewBox="0 0 1200 1200" xmlns="http://www.w3.org/2000/svg" role="img" aria-label="Conceptual model: Food, Physical Activity and Mind overlap at Sustained Weight Loss Maintenance, surrounded by rings for Make it Easy, Align with Identity, and Virtual Support and Social Connection">
  <defs>
    <marker id="arrowhead" viewBox="0 0 10 10" refX="9" refY="5" markerWidth="7" markerHeight="7" orient="auto">
      <path d="M0 1 L10 5 L0 9 Z" fill="#474747"/>
    </marker>
    <path id="arc-support-top" d="M229.0 741.7 A377.5 377.5 0 0 1 653.5 253.2"/>
    <path id="arc-support-bottom" d="M722.2 1001.8 A400 400 0 0 0 982.0 693.8"/>
    <path id="arc-identity-top" d="M685.1 299.2 A340 340 0 0 1 894.6 771.9"/>
    <path id="arc-identity-bottom" d="M228.5 568.1 A364 364 0 0 0 395.1 933.7"/>
    <path id="arc-easy-top" d="M370.4 422.8 A297 297 0 0 1 807.0 424.3"/>
    <path id="arc-easy-bottom" d="M407.0 898.5 A328 328 0 0 0 772.8 896.0"/>
  </defs>

  <!-- framework rings -->
  <circle class="ring-dashed" cx="588" cy="625" r="411"/>
  <circle class="ring-band" cx="588" cy="625" r="352"/>
  <circle class="ring-dashed" cx="588" cy="625" r="291"/>

  <!-- ring labels -->
  <text class="ring-text"><textPath href="#arc-support-top" textLength="777" lengthAdjust="spacing">Virtual Support and Social Connection <tspan class="sep">–</tspan> accessibility, community, shared accountability</textPath></text>
  <text class="ring-text"><textPath href="#arc-support-bottom" textLength="422" lengthAdjust="spacing">accessibility, community, shared accountability</textPath></text>
  <text class="ring-text"><textPath href="#arc-identity-top" textLength="587" lengthAdjust="spacing">Align with Identity <tspan class="sep">–</tspan> self-concept, Maintain IT model, internalization</textPath></text>
  <text class="ring-text"><textPath href="#arc-identity-bottom" textLength="426" lengthAdjust="spacing">self-concept, Maintain IT model, internalization</textPath></text>
  <text class="ring-text"><textPath href="#arc-easy-top" textLength="490" lengthAdjust="spacing">Make it Easy <tspan class="sep">–</tspan> habits, routines, environment, low friction</textPath></text>
  <text class="ring-text"><textPath href="#arc-easy-bottom" textLength="388" lengthAdjust="spacing">habits, routines, environment, low friction</textPath></text>

  <!-- domains -->
  <circle class="domain domain-food" cx="508" cy="578" r="141"/>
  <circle class="domain domain-activity" cx="671" cy="578" r="141"/>
  <circle class="domain domain-mind" cx="584" cy="708" r="141"/>

  <text class="domain-label" x="464" y="543">Food</text>
  <text class="domain-label" x="711" y="540">Physical</text>
  <text class="domain-label" x="711" y="563">Activity</text>
  <text class="domain-label" x="589" y="784">Mind</text>

  <text class="outcome-label" x="591" y="605">Sustained</text>
  <text class="outcome-label" x="591" y="622">Weight Loss</text>
  <text class="outcome-label" x="591" y="639">Maintenance</text>

  <!-- vulnerabilities -->
  <text class="vulnerability" transform="translate(411 450) rotate(-22)">Appetite Resurgence</text>
  <text class="vulnerability" transform="translate(778 456) rotate(40)">Metabolic Inflexibility</text>
  <text class="vulnerability" transform="translate(591 876) rotate(-3)">Suboptimal Mindstate</text>

  <line class="pointer" x1="409" y1="459" x2="449" y2="521"/>
  <line class="pointer" x1="770" y1="461" x2="731" y2="521"/>
  <line class="pointer" x1="588" y1="862" x2="588" y2="795"/>
</svg>
</body>
</html>
```